Chimney Service company needs new business card design

We need a updated business card with our new logo added. We provide a full range of chimney services throughout Vermont and New Hampshire. The business card will be one sided and color. Attached is our current business card another document showing all the information we would like on the card.
We dont like a lot of flashy colors.... here is a link to our website to get an idea of our branding www.flueguardianvt.example

Target Market(s)

homeowners

Industry/Entity Type

Business

Contact Information for Business Card

See attached sheet for content.

Font styles to use
Serif
Sans Serif

Requirements
Must have
• all information provided on separate sheet
Should not have
• Additional information that may clogg up design

```html
<!DOCTYPE html>
<html lang="en">
<head>
<meta charset="utf-8">
<title>Flue Guardian – Business Card</title>
<link rel="stylesheet" href="https://fonts.googleapis.com/css2?family=Tinos:ital,wght@0,400;1,400&display=swap">
<style>
  :root {
    --page: #e6e6e6;
    --card-white: #ffffff;
    --charcoal: #2e2e30;
    --charcoal-light: #3a3a3c;
    --brick-red: #a51e22;
    --ink: #1f1f1f;
  }
  * { margin: 0; padding: 0; box-sizing: border-box; }
  html, body { width: 1200px; height: 873px; overflow: hidden; background: var(--page); }
  .stage { position: relative; width: 1200px; height: 873px; }

  .card {
    position: absolute; left: 250px; width: 700px; height: 400px;
    border-radius: 18px; overflow: hidden;
    box-shadow: 0 6px 18px rgba(0,0,0,.18);
  }

  /* Back side */
  .card-back { top: 24px; background: linear-gradient(135deg, var(--charcoal-light), var(--charcoal)); }
  .back-name {
    position: absolute; left: 0; right: 0; top: 180px; text-align: center;
    font-family: "Tinos", serif; font-weight: 400; font-size: 32px; letter-spacing: 2px;
    color: #ffffff;
  }

  /* Front side */
  .card-front { top: 449px; background: var(--card-white); }
  .front-name {
    position: absolute; left: 30px; top: 146px; width: 310px; text-align: center;
    font-family: "Tinos", serif; font-weight: 400; font-size: 30px; letter-spacing: 2px;
    color: var(--charcoal);
  }

  .service-list { position: absolute; left: 378px; top: 34px; list-style: none; }
  .service-list li {
    font-family: "Tinos", serif; font-size: 17px; color: var(--ink);
    height: 31px; display: flex; align-items: center; gap: 10px;
  }
  .service-list li::before {
    content: ""; width: 9px; height: 9px; background: var(--brick-red); border-radius: 50%;
  }

  .bands { position: absolute; inset: 0; }
  .strip-text {
    position: absolute; font-family: "Tinos", serif; font-style: italic; font-size: 17px; color: #ffffff;
  }
  .strip-family { left: 430px; top: 207px; }
  .strip-insured { left: 58px; top: 243px; }

  .phone {
    position: absolute; left: 0; width: 335px; top: 282px;
    display: flex; align-items: center; justify-content: center; gap: 12px;
    font-family: "Tinos", serif; font-size: 30px; color: #ffffff;
  }
  .contact {
    position: absolute; left: 368px; top: 246px; list-style: none;
    font-family: "Tinos", serif; font-size: 17px; color: #ffffff;
  }
  .contact li { display: flex; align-items: center; gap: 9px; height: 24px; }
  .service-area {
    position: absolute; left: 0; right: 0; top: 356px; text-align: center;
    font-family: "Tinos", serif; font-size: 17px; color: #ffffff;
  }
</style>
</head>
<body>
<main class="stage">

  <section class="card card-back" aria-label="Business card back">
    <p class="back-name">FLUE GUARDIAN</p>
  </section>

  <section class="card card-front" aria-label="Business card front">
    <svg class="bands" width="700" height="400" viewBox="0 0 700 400">
      <polygon points="352,200 700,200 700,235 338,235" fill="var(--charcoal)"/>
      <polygon points="0,235 338,235 326,270 0,270" fill="var(--charcoal)"/>
      <polygon points="338,235 700,235 700,330 0,330 0,270 326,270" fill="var(--brick-red)"/>
      <line x1="348" y1="246" x2="348" y2="320" stroke="rgba(255,255,255,.55)" stroke-width="1"/>
      <rect x="0" y="330" width="700" height="4" fill="#ffffff"/>
      <rect x="0" y="334" width="700" height="66" fill="var(--charcoal)"/>
    </svg>

    <p class="front-name">FLUE GUARDIAN</p>

    <ul class="service-list">
      <li>Full Masonry Services</li>
      <li>Historic chimney restoration</li>
      <li>Stainless steel liners</li>
      <li>New Chimney installations</li>
      <li>FSCA Certified Chimney sweeps</li>
    </ul>

    <p class="strip-text strip-family">Family owned and operated</p>
    <p class="strip-text strip-insured">Fully Insured – Free Estimates</p>

    <p class="phone">
      <svg width="20" height="20" viewBox="0 0 24 24" aria-hidden="true"><path fill="#fff" d="M6.6 10.8a15.1 15.1 0 0 0 6.6 6.6l2.2-2.2c.3-.3.7-.4 1-.2 1.1.4 2.3.6 3.6.6.6 0 1 .4 1 1V20c0 .6-.4 1-1 1A17 17 0 0 1 3 4c0-.6.4-1 1-1h3.5c.6 0 1 .4 1 1 0 1.3.2 2.5.6 3.6.1.3 0 .7-.2 1z"/></svg>
      802-555-0147
    </p>

    <ul class="contact">
      <li>
        <svg width="14" height="11" viewBox="0 0 14 11" aria-hidden="true"><rect x="0.5" y="0.5" width="13" height="10" fill="none" stroke="#fff"/><polyline points="0.5,0.5 7,6 13.5,0.5" fill="none" stroke="#fff"/></svg>
        info@flueguardianvt.example
      </li>
      <li>
        <svg width="14" height="14" viewBox="0 0 14 14" aria-hidden="true"><circle cx="7" cy="7" r="6" fill="#fff"/></svg>
        www.flueguardianvt.example
      </li>
    </ul>

    <p class="service-area">Serving Ridge and Lake Counties since 1996</p>
  </section>

</main>
</body>
</html>
```